Buch-Cover für Sonnenherz gesucht
Der Designer hat sich sehr schnell in meine Vorgaben eingearbeitet und gleichzeitig wertvolle Vorschläge zur Optimierung abgegeben. Das Ergebnis ist dadurch sogar besser geworden, als ich mir im Vorfeld ausgemalt hatte. 100% Weiterempfehlung.
Zielgruppe
Wir sind eine Firma die hochwertige Fitnessprodukte produziert und vertreibt. Unsere Zielgruppe sind gesundheitsbewusste Frauen ab Mitte 20 bis open end, die hohe Ansprüche an sich selbst stellen und sich für das Thema Selbstoptimierung interessieren.
Aufgabenstellung
Es soll ein Hardcover gestaltet werden.
Buchtitel: Sonnenherz, Untertitel: Das Erwachen der Seele
Detaillierte Beschreibung der Projektanforderungen siehe Anhang Projektbeschreibung. Darüber hinaus bin ich auch für alternative Gestaltungs-Ideen offen.
Das Design soll der Käuferin folgendes vermitteln:
- Wertigkeit
- Positivität
und sie ein bisschen träumen lassen und natürlich neugierig auf den Inhalt machen.

```html
<!DOCTYPE html>
<html lang="de">
<head>
<meta charset="utf-8">
<title>Sonnenherz – Buchumschlag</title>
<link rel="stylesheet" href="https://fonts.googleapis.com/css2?family=Dancing+Script:wght@700&family=Kaushan+Script&family=Playfair+Display:ital,wght@1,700&family=Oswald:wght@400;500&family=Source+Sans+3:wght@400&family=Open+Sans:wght@400&display=swap">
<style>
  :root {
    --page: #ffffff;
    --teal-deep: #0f6f78;
    --teal: #1c8e92;
    --teal-dark: #0d3c57;
    --peach: #f4c7a4;
    --peach-light: #f8dcc0;
    --sand: #e9b98f;
    --dusk: #3a3a3e;
    --white: #ffffff;
    --cream: #fbf0e2;
    --orange: #c2582a;
    --gold: #f0c93a;
    --spine: #1a7d82;
  }
  * { margin: 0; padding: 0; box-sizing: border-box; }
  html, body { width: 1200px; height: 808px; overflow: hidden; background: var(--page); }
  .canvas { position: relative; width: 1200px; height: 808px; }
  .jacket {
    position: absolute; left: 43px; top: 30px; width: 1116px; height: 750px;
    display: flex; box-shadow: 0 6px 14px rgba(0,0,0,.35);
  }
  .back {
    position: relative; flex: 0 0 543px; width: 543px; height: 100%; overflow: hidden;
    background: linear-gradient(180deg, #2e6f86 0%, #b9a58f 14%, var(--peach) 30%, var(--sand) 40%, #7fb0a2 50%, var(--teal) 60%, var(--teal-deep) 100%);
  }
  .spine {
    position: relative; flex: 0 0 43px; width: 43px; height: 100%; overflow: hidden;
    background: linear-gradient(180deg, #1d8a8d, var(--spine));
    border-left: 1px solid rgba(255,255,255,.25);
    border-right: 1px solid rgba(0,0,0,.2);
  }
  .front {
    position: relative; flex: 0 0 530px; width: 530px; height: 100%; overflow: hidden;
  }
  .front-photo {
    position: absolute; inset: 0;
    background: linear-gradient(180deg, var(--teal-dark) 0%, #5d7f8c 12%, var(--peach-light) 30%, var(--peach) 45%, #d8a98a 56%, #8c7e70 66%, #5a5650 78%, var(--dusk) 100%);
  }
  .back-title {
    position: absolute; left: 0; right: 0; top: 95px; text-align: center;
    font-family: 'Dancing Script', cursive; font-size: 76px; color: var(--white);
    text-shadow: 0 0 14px rgba(255,255,255,.5);
  }
  .back-heading {
    position: absolute; left: 0; right: 0; top: 310px; text-align: center;
    font-family: 'Oswald', sans-serif; font-weight: 400; font-size: 29px;
    letter-spacing: 3px; color: var(--cream);
  }
  .blurb {
    position: absolute; left: 44px; width: 456px; top: 372px;
    font-family: 'Source Sans 3', sans-serif; font-size: 13px; line-height: 20px;
    color: var(--white); text-align: justify; hyphens: auto;
  }
  .blurb p + p { margin-top: 18px; }
  .spine-text {
    position: absolute; left: 50%; top: 18px;
    transform-origin: 0 0; transform: rotate(90deg) translateY(-50%);
    white-space: nowrap; display: flex; align-items: baseline; gap: 14px;
  }
  .spine-author { font-family: 'Playfair Display', serif; font-style: italic; font-weight: 700; font-size: 17px; color: var(--white); }
  .spine-title { font-family: 'Oswald', sans-serif; font-size: 24px; letter-spacing: 2px; color: var(--white); font-weight: 500; }
  .spine-sub { font-family: 'Kaushan Script', cursive; font-size: 22px; color: var(--gold); }
  .publisher {
    position: absolute; top: 32px; left: 0; right: 0; display: flex; justify-content: center; align-items: center; gap: 8px;
    font-family: 'Open Sans', sans-serif; font-size: 16px; color: var(--white); letter-spacing: 1px;
  }
  .publisher-dot { width: 12px; height: 12px; border-radius: 50%; background: var(--white); }
  .author {
    position: absolute; top: 84px; left: 0; right: 0; text-align: center;
    font-family: 'Playfair Display', serif; font-style: italic; font-weight: 700; font-size: 38px; color: var(--white);
  }
  .title {
    position: absolute; top: 150px; left: 0; right: 0; text-align: center;
    font-family: 'Dancing Script', cursive; font-size: 110px; line-height: 1; color: var(--white);
    text-shadow: 0 0 18px rgba(255,255,255,.45);
  }
  .subtitle {
    position: absolute; top: 306px; left: 0; right: 0; text-align: center;
    font-family: 'Kaushan Script', cursive; font-size: 31px; line-height: 36px; color: var(--orange);
  }
</style>
</head>
<body>
<div class="canvas">
  <div class="jacket">
    <section class="back" role="img" aria-label="Sonnenuntergang mit Lichtreflexen, in Türkis übergehend">
      <div class="back-title">Sonnenherz</div>
      <h2 class="back-heading">Was zählt wirklich?</h2>
      <div class="blurb">
        <p>Ich habe mich oft gefragt: Wie soll ich bloß die Liebe und Bestätigung, die mir damals in meiner Kindheit verwehrt blieben, „nachholen“? Lösungsansätze für mein Problem hatte ich in der Vergangenheit durchaus: Ich versuchte das Loch mit Hilfe zur Selbsthilfe, Erfolg im Job und Konsum zu stopfen. Und meine Partner mussten auch für so einiges herhalten.</p>
        <p>Von Gott wollte ich lange nichts wissen. Schließlich hatte er es zugelassen, dass mir sehr viel Unheil in meinem Leben widerfahren ist. Und deshalb war ich echt wütend auf ihn.</p>
        <p>Heutzutage bin ich mir sicher, dass ich mit dieser Denkweise meine Lebenszeit verschwendet habe. Letzten Sommer begriff ich endlich: im Leben gilt die gleiche Gesetzmäßigkeit wie beim Autofahren. Der Rückspiegel ist so klein und die Frontscheibe so groß, weil das, was vor uns liegt, viel wichtiger ist als das, was hinter uns liegt. Aufgrund dieser Erkenntnis entschied ich mich, einen völlig neuen Weg einzuschlagen und wagte mich auf eine spannende Reise, die mein Leben für immer veränderte …</p>
      </div>
    </section>
    <section class="spine">
      <div class="spine-text">
        <span class="spine-author">Mara Feltkamp</span>
        <span class="spine-title">SONNENHERZ</span>
        <span class="spine-sub">Das Erwachen der Seele</span>
      </div>
    </section>
    <section class="front">
      <div class="front-photo" role="img" aria-label="Frau von hinten am Steuer eines Cabrios auf einem Feldweg im Abendlicht"></div>
      <div class="publisher"><span class="publisher-dot"></span><span>Lumenhaus</span></div>
      <div class="author">Mara Feltkamp</div>
      <h1 class="title">Sonnenherz</h1>
      <div class="subtitle">Das Erwachen<br>der Seele</div>
    </section>
  </div>
</div>
</body>
</html>
```